Marks of Dunmore business card design

I need a clean, professional looking design using the attached logo with a bright green/ gray/dark gray/black colors. Maybe even an orange accent if it looks good. I am open to slight changes in the logo if needed. Details below on the info on what should be on the cards. We are a sign company in Ft. Lauderdale FL that specializes in yacht lettering on multi million dollar yachts.

Target Market(s)

marine industry, yachts

Industry/Entity Type

Business

Colors
9bcb3c
000000
606060
f37122

Requirements
Must have
• address: 2847 W. Harlow Rd.
• Pompano Beach, FL 33417
• Phone: 954-518-3046
• email/website: marksofdunmore@mailvista.net MarksofDunmore.net
Nice to have
• I would like it very clean and simple but professional looking. Nice layout and would prefer a darker background. Orange highlight only if it works.
Should not have
• Nothing fancy.

```html
<!DOCTYPE html>
<html lang="en">
<head>
<meta charset="utf-8">
<title>Marks of Dunmore — Business Card</title>
<link rel="stylesheet" href="https://fonts.googleapis.com/css2?family=Oxygen:wght@400;700&display=swap">
<style>
  :root {
    --brand-green: #8cc63f;
    --ink: #222222;
    --card-paper: #f4f2ee;
    --backdrop: #d9d6d1;
  }
  * { margin: 0; padding: 0; box-sizing: border-box; }
  html, body {
    width: 1200px;
    height: 1200px;
    overflow: hidden;
    background: var(--backdrop);
  }
  .canvas {
    width: 1200px;
    height: 1200px;
    display: flex;
    align-items: center;
    justify-content: center;
  }
  .business-card {
    position: relative;
    width: 1000px;
    height: 572px;
    background: var(--card-paper);
    box-shadow: 0 10px 30px rgba(0,0,0,0.18);
    font-family: "Oxygen", sans-serif;
    color: var(--ink);
  }
  .brand-name {
    position: absolute;
    top: 70px;
    left: 0;
    right: 0;
    text-align: center;
    font-weight: 700;
    font-size: 84px;
    letter-spacing: 1px;
    color: var(--brand-green);
    line-height: 1;
  }
  .address {
    position: absolute;
    top: 215px;
    left: 0;
    right: 0;
    text-align: center;
    font-size: 34px;
    line-height: 1.3;
  }
  .divider {
    position: absolute;
    left: 0;
    right: 0;
    top: 420px;
    height: 4px;
    background: var(--brand-green);
  }
  .contact-item {
    position: absolute;
    width: 333px;
    text-align: center;
  }
  .contact-item svg {
    position: absolute;
    top: 345px;
    left: 50%;
    transform: translateX(-50%);
  }
  .contact-item .label {
    position: absolute;
    top: 460px;
    left: 0;
    right: 0;
    font-size: 28px;
    white-space: nowrap;
  }
  .contact-email { left: 0; top: 0; }
  .contact-phone { left: 333px; top: 0; }
  .contact-web { left: 667px; top: 0; }
  .email-label { font-size: 24px !important; }
</style>
</head>
<body>
<div class="canvas">
  <div class="business-card">
    <div class="brand-name">Marks of Dunmore</div>

    <div class="address">
      2847 W. Harlow Rd.<br>
      Pompano Beach, FL 33417
    </div>

    <div class="divider"></div>

    <div class="contact-item contact-email">
      <svg width="66" height="48" viewBox="0 0 66 48" aria-hidden="true">
        <rect x="2" y="2" width="62" height="44" fill="var(--brand-green)"/>
        <polyline points="2,2 33,26 64,2" fill="none" stroke="var(--card-paper)" stroke-width="3"/>
        <line x1="2" y1="46" x2="25" y2="20" stroke="var(--card-paper)" stroke-width="3"/>
        <line x1="64" y1="46" x2="41" y2="20" stroke="var(--card-paper)" stroke-width="3"/>
      </svg>
      <div class="label email-label">marksofdunmore@mailvista.net</div>
    </div>

    <div class="contact-item contact-phone">
      <svg width="70" height="62" viewBox="0 0 70 62" aria-hidden="true">
        <path d="M4 18 Q35 -2 66 18 L60 26 L48 22 L48 16 Q35 12 22 16 L22 22 L10 26 Z" fill="var(--brand-green)"/>
        <path d="M20 26 L50 26 L62 58 L8 58 Z" fill="var(--brand-green)"/>
        <circle cx="35" cy="42" r="10" fill="var(--card-paper)"/>
        <circle cx="35" cy="42" r="4" fill="var(--brand-green)"/>
      </svg>
      <div class="label">954-518-3046</div>
    </div>

    <div class="contact-item contact-web">
      <svg width="64" height="64" viewBox="0 0 64 64" aria-hidden="true">
        <g fill="none" stroke="var(--brand-green)" stroke-width="3">
          <circle cx="32" cy="32" r="28"/>
          <ellipse cx="32" cy="32" rx="12" ry="28"/>
          <line x1="32" y1="4" x2="32" y2="60"/>
          <line x1="4" y1="32" x2="60" y2="32"/>
          <path d="M9 18 H55 M9 46 H55"/>
        </g>
      </svg>
      <div class="label">MarksofDunmore.net</div>
    </div>
  </div>
</div>
</body>
</html>
```